The Weave of Brightfold

We are running an international event in Switzerland on "Transmedia" with some of the hottest names in this hot media space ...

There will be 15 Keynote addresses and we are paying to have them professionally transcribed, copywritten, and proof-read to be published in an eBook.

The 15 Keynotes reference a huge number of global media brands - have a look: www.plimvoracast.com

We want a riveting, beautifully designed eBook cover and layout strategy - with the idea that this will be first of a series we will publish on different "Creative Industries" professional development issues - so MOST important is to think of the ARCHITECTURE of the artwork, as well as the graphic design ... think of the idea of an "imprint" in traditional book publishing - the architecture will remain the same, but the artwork and imagry will change each time.

Core values: Global media, Excellence, World's Best practitioners, Know How-to, Instant Inside Knowledge.

Target Market(s)

Professional Development for International Creative Industries Practitioners.

Industry/Entity Type

Graphic Design

Requirements
Must have
• Should be re-purposable across all other forms of media: it's "Transmedia", right? It should incorporate artwork, design, operate as a logo, typeface and font, and a basic imprint for a series of eBooks

The most important consideration in buying an Book is the Table of Content and the authors (we've got that in gold!) - The second-most important consideration is the artwork on the cover ... it has to be instantly convincing.

```html
<!DOCTYPE html>
<html lang="en">
<head>
<meta charset="utf-8">
<title>The Weave of Brightfold</title>
<link rel="stylesheet" href="https://fonts.googleapis.com/css2?family=Bebas+Neue&display=swap">
<style>
  :root {
    --wall-top: #3a3a3a;
    --wall-mid: #262626;
    --floor-light: #d9b98c;
    --floor-dark: #b98f5c;
    --panel-light: #f4f4f4;
    --panel-edge: #c9c9c9;
    --ink: #0a0a0a;
    --paper: #ffffff;
    --band-a: #d8345f;
    --band-b: #2ba7a0;
    --band-c: #f2b33d;
    --band-d: #4a4fa3;
  }
  html, body {
    margin: 0;
    padding: 0;
    overflow: hidden;
    background: var(--paper);
  }
  .cover {
    position: relative;
    width: 917px;
    height: 1200px;
    overflow: hidden;
    font-family: "Bebas Neue", "Arial Narrow", sans-serif;
  }
  .gallery-scene {
    position: absolute;
    left: 0;
    top: 0;
    width: 917px;
    height: 980px;
    background: linear-gradient(
      to bottom,
      var(--wall-top) 0%,
      var(--wall-mid) 40%,
      var(--wall-mid) 77%,
      var(--floor-light) 78%,
      var(--floor-dark) 100%
    );
  }
  .title-panel {
    position: absolute;
    left: 96px;
    top: 169px;
    width: 709px;
    height: 479px;
    background: radial-gradient(ellipse at 50% 30%, var(--panel-light) 0%, #e2e2e2 60%, var(--panel-edge) 100%);
    display: flex;
    flex-direction: column;
    justify-content: center;
    align-items: center;
  }
  .series-title {
    margin: 0;
    color: var(--ink);
    font-weight: 400;
    font-size: 134px;
    line-height: 0.98;
    text-align: center;
    letter-spacing: 2px;
  }
  .series-title span { display: block; }
  .pattern-band {
    position: absolute;
    left: 0;
    top: 980px;
    width: 917px;
    height: 220px;
    background: linear-gradient(
      120deg,
      var(--band-a) 0%,
      var(--band-c) 30%,
      var(--band-b) 60%,
      var(--band-d) 100%
    );
  }
  .keynote-label {
    position: absolute;
    left: 187px;
    top: 1006px;
    width: 540px;
    height: 194px;
    background: var(--ink);
    color: var(--paper);
    text-align: center;
    box-sizing: border-box;
    padding-top: 6px;
  }
  .keynote-count {
    margin: 0;
    font-weight: 400;
    font-size: 138px;
    line-height: 1;
    letter-spacing: 2px;
  }
  .keynote-tagline {
    margin: 0;
    font-weight: 400;
    font-size: 38px;
    line-height: 1;
    letter-spacing: 1px;
  }
</style>
</head>
<body>
  <main class="cover">
    <div class="gallery-scene" role="img" aria-label="Gallery room with a dark wall, ceiling spotlights, a pale wooden floor and a white bench"></div>
    <div class="title-panel">
      <h1 class="series-title"><span>The Weave of</span><span>Brightfold</span></h1>
    </div>
    <div class="pattern-band" role="img" aria-label="Colourful mosaic pattern of small triangles"></div>
    <div class="keynote-label">
      <p class="keynote-count">15 Keynote</p>
      <p class="keynote-tagline">World's Best Practitioners</p>
    </div>
  </main>
</body>
</html>
```